design 3 a5 leaflets for tradesmen such as plumbers

I am looking for 3 flyers to be made for advertising painters and tradesmen. They are the type that have 10 - 12 tear away phone numbers.
I want 3 designs so that i can out compete the competition dunmore kettle style. The winners will design 3 they don't need to be top class as the competition are generally home made. there will be three winners please use the phone numbers in the upload i gave you but advertise plumber on one leaflet and electrician saying local man ,competitive rates etc etc

```html
<!DOCTYPE html>
<html lang="en">
<head>
<meta charset="utf-8">
<title>Looking for Plumbers – Leaflet</title>
<link rel="stylesheet" href="https://fonts.googleapis.com/css2?family=Arvo:wght@700&family=Lato:wght@300;400;700&display=swap">
<style>
  :root {
    --brand-blue: #1b9fe0;
    --frame-blue: #35a9e3;
    --ink: #111111;
    --paper: #ffffff;
    --paper-shade: #eceef0;
    --dash: #4fb4e6;
  }
  * { box-sizing: border-box; margin: 0; padding: 0; }
  html, body { width: 849px; height: 1200px; overflow: hidden; background: var(--paper); }
  .leaflet {
    position: relative;
    width: 849px;
    height: 1200px;
    border: 5px solid var(--frame-blue);
    background: radial-gradient(ellipse at 50% 30%, var(--paper) 40%, var(--paper-shade) 100%);
    font-family: 'Lato', sans-serif;
    overflow: hidden;
  }
  .headline {
    position: absolute;
    top: 42px; left: 0; width: 100%;
    text-align: center;
    font-family: 'Arvo', serif;
    font-weight: 700;
    font-size: 100px;
    line-height: 1;
    color: var(--brand-blue);
    letter-spacing: 2px;
  }
  .tool-artwork {
    position: absolute;
    top: 200px; left: 94px;
    width: 658px; height: 190px;
  }
  .trade-band {
    position: absolute;
    top: 414px; left: -5px; width: 849px; height: 134px;
    background: var(--brand-blue);
    display: flex; align-items: center; justify-content: center;
  }
  .trade-band h2 {
    font-family: 'Arvo', serif;
    font-weight: 700;
    font-size: 108px;
    line-height: 1;
    color: var(--paper);
    letter-spacing: 2px;
  }
  .promise {
    position: absolute;
    top: 568px; left: 0; width: 100%;
    text-align: center;
    font-size: 28px;
    font-weight: 400;
    color: var(--ink);
  }
  .call-box {
    position: absolute;
    top: 612px; left: 43px; width: 763px; height: 138px;
    background: var(--brand-blue);
    border: 4px solid var(--paper);
    box-shadow: 0 0 0 1px #c9d3da, 0 3px 6px rgba(0,0,0,0.25);
    text-align: center;
    color: var(--paper);
  }
  .call-box .call-prompt {
    margin-top: 12px;
    font-size: 41px; font-weight: 300; line-height: 1.1;
  }
  .call-box .call-number {
    font-size: 68px; font-weight: 400; line-height: 1; letter-spacing: 2px;
  }
  .selling-points {
    position: absolute;
    top: 770px; left: 38px;
    list-style: none;
    font-family: 'Arvo', serif;
    font-weight: 700;
    font-size: 41px;
    line-height: 58px;
    color: var(--brand-blue);
  }
  .selling-points li::before { content: "\2022"; margin-right: 14px; }
  .trade-range {
    position: absolute;
    top: 766px; left: 575px;
    font-size: 20px; color: var(--ink);
  }
  .agency-name {
    position: absolute;
    top: 870px; left: 575px;
    font-size: 26px; font-weight: 400; line-height: 1.2;
    color: var(--ink);
  }
  .trade-list {
    position: absolute;
    top: 916px; left: 27px;
    font-size: 16px; line-height: 21px; color: var(--ink);
  }
  .tear-strip {
    position: absolute;
    top: 968px; left: 0; width: 839px; height: 232px;
    border-top: 2px dashed var(--dash);
    display: flex;
  }
  .tear-tab {
    flex: 1;
    border-left: 2px dashed var(--dash);
    display: flex; align-items: center; justify-content: center;
  }
  .tear-tab:first-child { border-left: none; }
  .tear-tab span {
    writing-mode: vertical-rl;
    transform: rotate(180deg);
    font-size: 24px; letter-spacing: 1px; color: var(--ink);
  }
</style>
</head>
<body>
<main class="leaflet">
  <h1 class="headline">LOOKING FOR</h1>

  <svg class="tool-artwork" role="img" aria-label="Illustration of a blue adjustable spanner" viewBox="0 0 658 190">
    <defs>
      <linearGradient id="tool-tone" x1="0" y1="0" x2="1" y2="0">
        <stop offset="0" stop-color="#1b9fe0" stop-opacity="0.35"/>
        <stop offset="0.5" stop-color="#1b9fe0" stop-opacity="0.55"/>
        <stop offset="1" stop-color="#1b9fe0" stop-opacity="0.35"/>
      </linearGradient>
    </defs>
    <rect x="0" y="0" width="658" height="190" rx="18" fill="url(#tool-tone)"/>
  </svg>

  <div class="trade-band"><h2>PLUMBERS</h2></div>

  <p class="promise">WE WILL HELP YOU FIND THE BEST FOR LESS</p>

  <div class="call-box">
    <p class="call-prompt">JUST CALL US TODAY</p>
    <p class="call-number">0861449027</p>
  </div>

  <ul class="selling-points">
    <li>Local Men</li>
    <li>Competitive Rates</li>
  </ul>

  <p class="trade-range">FOR ANY TRADE A – Z</p>

  <p class="agency-name">Keystone Property</p>

  <p class="trade-list">Plumbers, Electricians, Handymen, Carpenters,<br>Plasterers, Tilers, Appliance Repairers, Cleaners Etc.</p>

  <div class="tear-strip">
    <div class="tear-tab"><span>0861449027</span></div>
    <div class="tear-tab"><span>0861449027</span></div>
    <div class="tear-tab"><span>0861449027</span></div>
    <div class="tear-tab"><span>0861449027</span></div>
    <div class="tear-tab"><span>0861449027</span></div>
    <div class="tear-tab"><span>0861449027</span></div>
    <div class="tear-tab"><span>0861449027</span></div>
    <div class="tear-tab"><span>0861449027</span></div>
    <div class="tear-tab"><span>0861449027</span></div>
    <div class="tear-tab"><span>0861449027</span></div>
    <div class="tear-tab"><span>0861449027</span></div>
    <div class="tear-tab"><span>0861449027</span></div>
  </div>
</main>
</body>
</html>
```